web and logo design for insurance quote site

i want a quoteform site simimar to brimtallow.com i have a site up now @ kvbrimtallow.com, its functional but not attractive

Target Market(s)

people looking to get a home, auto or life insurance quote

Industry/Entity Type

Insurance

Number of Pages Required

1 page

Requirements
Must have
• great form that gathers all the information and emails the form to me
Nice to have
• nice eye catching art design thatI can have printed on business cards to send poeople to the site

```html
<!DOCTYPE html>
<html lang="en">
<head>
<meta charset="utf-8">
<title>KVBrimtallow – Free Insurance Quotes</title>
<link rel="stylesheet" href="https://fonts.googleapis.com/css2?family=Arimo:wght@400;700&display=swap">
<style>
  :root {
    --sky-top: #cfe4f3;
    --sky-mid: #eaf3fa;
    --page: #ffffff;
    --ink: #1a1a1a;
    --ink-soft: #333333;
    --logo-grey: #3a3a3a;
    --brand-blue: #1f8fd6;
    --brand-blue-dark: #126fb0;
    --panel-light: #e6f2fa;
    --panel-mid: #c8e3f4;
    --nav-dark: #2b2b2b;
    --btn-top: #ffe066;
    --btn-bottom: #f5b400;
    --btn-edge: #b78200;
    --footer-top: #4a4a4a;
    --footer-bottom: #1e1e1e;
    --footer-text: #f2f2f2;
    --phone-orange: #f08a00;
    --phone-yellow: #ffc62e;
  }
  * { box-sizing: border-box; margin: 0; padding: 0; }
  html, body { width: 1200px; height: 770px; overflow: hidden; }
  body {
    font-family: "Arimo", Arial, sans-serif;
    color: var(--ink);
    background: var(--page);
  }
  .canvas {
    position: relative;
    width: 1200px;
    height: 770px;
    overflow: hidden;
    background: linear-gradient(180deg, var(--sky-top) 0px, var(--sky-mid) 160px, var(--page) 330px, var(--page) 100%);
  }
  .abs { position: absolute; }

  /* header */
  .brand {
    left: 137px; top: 30px;
    display: flex; align-items: center; gap: 10px;
    font-size: 38px; font-weight: 700; color: var(--logo-grey);
    letter-spacing: -0.5px;
  }
  .brand-square {
    width: 30px; height: 30px; background: var(--brand-blue); border-radius: 4px;
  }
  .phone {
    left: 858px; top: 40px;
    display: flex; align-items: center; gap: 14px;
    font-size: 22px; font-weight: 700; color: var(--ink-soft);
  }

  /* nav */
  .nav-home {
    left: 143px; top: 117px; width: 113px; height: 45px;
  }
  .nav-home span {
    position: absolute; left: 0; top: 0; width: 113px; height: 45px;
    display: flex; align-items: center; justify-content: center;
    color: #fff; font-weight: 700; font-size: 17px;
  }
  .nav-contact {
    left: 292px; top: 129px; font-weight: 700; font-size: 17px; color: var(--ink);
  }

  /* quote form */
  .form-title { left: 139px; top: 204px; font-size: 23px; font-weight: 700; }
  .type-select {
    left: 137px; top: 248px; width: 368px; height: 36px;
    border: 1px solid #8a8a8a; background: #fff;
    display: flex; align-items: center; justify-content: space-between;
  }
  .type-select .label { padding-left: 8px; font-size: 16px; color: var(--ink-soft); }
  .type-select .arrow {
    width: 38px; height: 34px; background: linear-gradient(#8d8d8d, #6b6b6b);
    display: flex; align-items: center; justify-content: center;
  }
  .quote-btn {
    left: 138px; top: 299px; width: 145px; height: 35px;
    border-radius: 8px; border: 1px solid var(--btn-edge);
    background: linear-gradient(var(--btn-top), var(--btn-bottom));
    font-size: 18px; font-weight: 700; color: var(--ink);
    display: flex; align-items: center; justify-content: center;
  }

  /* photo strip */
  .photo { box-shadow: 0 0 0 5px #fff, 0 2px 6px rgba(0,0,0,.15); }
  .photo-couple { left: 552px; top: 143px; width: 82px; height: 173px; background: linear-gradient(135deg, #f4efe8, #d9a98a 60%, #b97a5c); }
  .photo-house { left: 639px; top: 127px; width: 341px; height: 207px; background: linear-gradient(180deg, #8ec3ec 0%, #cfe3f2 35%, #4e5a52 50%, #3d5b3a 75%, #5f9a3a 100%); }
  .photo-car { left: 982px; top: 143px; width: 77px; height: 171px; background: linear-gradient(160deg, #bfd4e6, #8fa3b3 50%, #e8eef2 80%); }
  .reflect { height: 55px; background: linear-gradient(180deg, rgba(200,215,225,.45), rgba(255,255,255,0)); }

  /* body copy */
  .copy { left: 134px; width: 570px; font-size: 14px; line-height: 18px; color: var(--ink); }
  .copy h2 { font-weight: 400; color: var(--brand-blue); font-size: 20px; line-height: 24px; margin-bottom: 10px; }
  .welcome { top: 406px; }
  .request { top: 521px; }

  /* saving panel */
  .save-panel {
    left: 770px; top: 411px; width: 292px; height: 198px;
    border: 1px solid #7fb6da; border-radius: 14px;
    background: linear-gradient(180deg, var(--panel-light), var(--panel-mid));
    box-shadow: 0 14px 14px -10px rgba(160,180,195,.5);
  }
  .save-panel .head {
    position: absolute; left: 0; top: 0; width: 290px; height: 38px;
    border-radius: 13px 13px 0 0;
    background: linear-gradient(var(--brand-blue), var(--brand-blue-dark));
    color: #fff; font-weight: 700; font-size: 20px; padding: 7px 0 0 20px;
  }
  .save-panel .tail { position: absolute; left: 210px; top: 37px; }
  .save-panel .icon { position: absolute; left: 20px; top: 60px; }
  .save-panel p {
    position: absolute; left: 101px; top: 64px; width: 180px;
    font-size: 14px; line-height: 19px; color: var(--ink);
  }

  /* footer */
  .footer {
    left: 0; top: 664px; width: 1200px; height: 106px;
    background: linear-gradient(var(--footer-top), var(--footer-bottom));
  }
  .footer-text {
    position: absolute; left: 138px; top: 14px;
    font-size: 14px; line-height: 19px; color: var(--footer-text);
  }
  .footer-brand {
    position: absolute; left: 780px; top: 30px;
    display: flex; align-items: center; gap: 10px;
    font-size: 36px; font-weight: 700; color: #fff; letter-spacing: -0.5px;
  }
  .footer-brand .brand-square { background: #fff; }
</style>
</head>
<body>
<div class="canvas">

  <header>
    <div class="abs brand"><span class="brand-square"></span>kvbrimtallow.com</div>
    <div class="abs phone">
      <svg width="38" height="38" viewBox="0 0 38 38" aria-hidden="true">
        <circle cx="19" cy="19" r="18" fill="var(--phone-orange)"/>
        <circle cx="19" cy="19" r="14" fill="var(--phone-yellow)"/>
        <path d="M14 11c1-1 2-1 3 0l2 3c.5 1 0 2-1 2.5-.5.3-.5 1 0 2l2 2.5c.7.8 1.3.8 2 .3 1-.8 2-.8 2.6 0l2 2.2c.8 1 .5 2-.5 2.8-3 2.2-7 .2-10.5-4.3S11.5 14 14 11z" fill="#7a3a00"/>
      </svg>
      555 014 2288
    </div>
  </header>

  <nav>
    <div class="abs nav-home">
      <svg width="113" height="52" viewBox="0 0 113 52" aria-hidden="true">
        <rect x="0" y="0" width="113" height="45" rx="7" fill="var(--nav-dark)"/>
        <path d="M49 44 L56 52 L63 44 Z" fill="var(--nav-dark)"/>
      </svg>
      <span>Home</span>
    </div>
    <div class="abs nav-contact">Contact</div>
  </nav>

  <section class="quote-form">
    <h1 class="abs form-title">Get a Free Quote</h1>
    <div class="abs type-select">
      <span class="label">Choose Insurance Type</span>
      <span class="arrow">
        <svg width="22" height="18" viewBox="0 0 22 18" aria-hidden="true"><path d="M1 1 H21 L11 17 Z" fill="#2a2a2a"/></svg>
      </span>
    </div>
    <div class="abs quote-btn">GET QUOTE</div>
  </section>

  <section class="photo-strip">
    <div class="abs photo photo-couple" role="img" aria-label="Photo of a smiling couple"></div>
    <div class="abs reflect" style="left:552px;top:322px;width:82px;"></div>
    <div class="abs photo photo-car" role="img" aria-label="Photo of a white car on the road"></div>
    <div class="abs reflect" style="left:982px;top:320px;width:77px;"></div>
    <div class="abs photo photo-house" role="img" aria-label="Photo of a two-storey family home with a lawn"></div>
    <div class="abs reflect" style="left:639px;top:340px;width:341px;"></div>
  </section>

  <section class="abs copy welcome">
    <h2>Welcome</h2>
    <p>At KVBrimtallow , We are dedicated to offering a level of service that will result in lasting relationships with clients. our focus is on helping you find the best possible protection for yourself, your family, or your business at the lowest possible cost.</p>
  </section>

  <section class="abs copy request">
    <h2>Request a Quote - Start Saving Today!</h2>
    <p>My online quote tool makes it easy for you to request a quote on Auto, Home Owner's/Renter's, Life, Health or Long Term Care insurance.</p>
  </section>

  <aside class="abs save-panel">
    <div class="head">Start Saving Today!</div>
    <svg class="tail" width="40" height="16" viewBox="0 0 40 16" aria-hidden="true"><path d="M0 0 H40 L8 16 Z" fill="var(--brand-blue-dark)"/></svg>
    <svg class="icon" width="70" height="80" viewBox="0 0 70 80" aria-hidden="true">
      <ellipse cx="35" cy="72" rx="28" ry="6" fill="#9fb9cc" opacity=".6"/>
      <circle cx="35" cy="33" r="31" fill="#1b8bd6"/>
      <circle cx="35" cy="33" r="25" fill="#4fb4f0"/>
      <text x="35" y="45" text-anchor="middle" font-family="Arimo, Arial, sans-serif" font-size="34" font-weight="700" fill="#fff">@</text>
    </svg>
    <p>If you prefer to discuss a quote by phone, please give me a call at <strong>(555) 014-2288</strong> or contact me by telephone or email to discuss your needs.</p>
  </aside>

  <footer class="abs footer">
    <div class="footer-text">
      Powered by&nbsp; FormHarbor.com<br>
      Website text Copyright© KVbrimtallow.com<br>
      Auto, Home, Life, Health, Long Term Care Insurance Agent, PHOENIX, AZ,<br>
      All rights reserved.
    </div>
    <div class="footer-brand"><span class="brand-square"></span>kvbrimtallow.com</div>
  </footer>

</div>
</body>
</html>
```